We are an Estate agency (Real estate)– looking for Christmas/winter theme leaflet

We are called ‘’HOLLIVERS’’ we are an estate agency based in England. We opened in 2020 in February, few weeks before Covid and we are now known as one of the fastest growing agencies in all of Brighton and Hove.
This is our first Christmas/winter leaflet and this kind of offer!
Offer is: if the client signs with us to sell their home from 1st December 2021 until 7th January 2022 they will receive 50% off HOLLIVERS fees.
I am looking for A5 two-sided leaflet. The first side should contain our branding, the offer. Also, maybe this: ‘’ Let us Treat you this Christmas’’ or maybe on the other side of leaflet, which will contain explanation of the offer, our office details etc. the back should also contain some design.
Our target market is higher end clients who own a property in Brighton and Hove and looking to sell. I would say target market 35+ years of age.
Our branding is clean, fresh and eye catching and that’s what leaflet should look like and represent.
I will insert our website link so you could have a look at the properties that we deal with too. I could also insert last leaflet which I designed and had a really positive response & feedback… maybe will give you some ideas.
I have inserted our brand guidelines. We use Hollivers in white or blue backgrounds as in guideline.
https://www.holliversestateagents.co.uk/
Hi guys,
Thank you for all your ideas so far, however just wanted to mention that I am looking for not so much ''in your face Christmas'' design - something subtle.
Needs to be classy, modern and eye catching - our target market is property owners 35+ years of age. Moreover, this offer needs to be perceived as one off opportunity.
35+ property owners

```html
<!DOCTYPE html>
<html lang="en">
<head>
<meta charset="utf-8">
<title>Hollivers – Christmas Leaflet</title>
<link rel="stylesheet" href="https://fonts.googleapis.com/css2?family=Ubuntu:wght@300;400;500;700&display=swap">
<style>
  :root{
    --backdrop:#0b0b0b;
    --sheet-dark:#1c1c1c;
    --brand-red:#c00000;
    --deep-red:#8a0000;
    --mid-red:#b00000;
    --white:#ffffff;
    --photo-sky:#8fa6bd;
    --photo-brick:#9a4a36;
  }
  *{margin:0;padding:0;box-sizing:border-box}
  html,body{width:1200px;height:900px;overflow:hidden;background:var(--backdrop)}
  body{position:relative;font-family:'Ubuntu',sans-serif;color:var(--white)}

  .page{position:absolute;top:146px;width:444px;height:630px;overflow:hidden}
  .page--back{left:159px;background:var(--sheet-dark)}
  .page--front{left:614px;background:linear-gradient(90deg,var(--deep-red) 0%,var(--mid-red) 35%,var(--mid-red) 55%,var(--deep-red) 100%)}

  .brand-name{position:absolute;font-weight:500;color:var(--white);letter-spacing:.18em;white-space:nowrap}
  .page--back .brand-name{left:23px;top:81px;font-size:13px}
  .page--front .brand-name{left:0;width:100%;text-align:center;top:185px;font-size:24px;letter-spacing:.2em}

  .accent-bar{position:absolute;left:0;top:114px;width:41px;height:328px;background:linear-gradient(180deg,var(--deep-red),var(--mid-red))}
  .photo-column{position:absolute;left:49px;top:114px;width:123px;display:flex;flex-direction:column;gap:1px}
  .photo{height:81.5px;background:linear-gradient(180deg,var(--photo-sky) 0%,#c9c2b8 45%,var(--photo-brick) 80%,#5c6b45 100%)}
  .photo--white-villa{background:linear-gradient(180deg,#6f93c4 0%,#e8e6e0 45%,#dcdcd6 75%,#7f8a6a 100%)}

  .headline{position:absolute;right:17px;top:24px;text-align:right;font-weight:700;color:var(--brand-red);font-size:72px;line-height:62px;letter-spacing:-1px}
  .offer{position:absolute;right:17px;top:213px;text-align:right;font-weight:300;color:var(--brand-red);font-size:15.5px;line-height:21.5px}
  .offer .offer-brand{color:var(--white);font-weight:400}

  .about-rule{position:absolute;left:204px;top:303px;width:3px;height:306px;background:var(--brand-red)}
  .about{position:absolute;left:225px;top:300px;width:204px}
  .about-title{font-weight:700;color:var(--brand-red);font-size:14.5px;line-height:18px;white-space:nowrap}
  .about-text{margin-left:2px;font-size:11.8px;line-height:18px;text-align:justify;font-weight:400}

  .contact-icons{position:absolute;left:222px;top:560px;width:18px;display:flex;flex-direction:column;gap:2px}
  .contact-icons svg{display:block;width:17px;height:14px}
  .contact-box{position:absolute;left:318px;top:555px;width:126px;height:53px;background:var(--brand-red)}
  .contact-lines{position:absolute;right:11px;top:3px;text-align:right;white-space:nowrap}
  .contact-phone{font-weight:500;font-size:14px;line-height:18px}
  .contact-line{font-size:11px;line-height:13px}

  .office-icon{position:absolute;left:20px;top:454px;width:26px;height:27px}
  .info{position:absolute;left:19px;font-size:10.5px;line-height:17px}
  .info-title{font-weight:500;font-size:12px;line-height:14px}
  .info--office{top:484px}
  .info--hours{top:532px}

  .front-tagline{position:absolute;left:43px;top:489px;font-weight:700;font-size:36px;line-height:34px;color:var(--white)}
</style>
</head>
<body>

<section class="page page--back" aria-label="Leaflet back">
  <div class="brand-name">HOLLIVERS</div>

  <div class="accent-bar"></div>
  <div class="photo-column">
    <div class="photo photo--white-villa" role="img" aria-label="Photo of a white detached villa on a sunny street"></div>
    <div class="photo" role="img" aria-label="Photo of a red-brick Victorian terrace with white bay windows"></div>
    <div class="photo" role="img" aria-label="Photo of a large red-brick detached house with gables"></div>
    <div class="photo" role="img" aria-label="Photo of a row of red-brick Edwardian houses with front gardens"></div>
  </div>

  <h1 class="headline">SELL<br>YOUR<br>HOME</h1>
  <p class="offer">from 1st December 2021 until<br>7th January 2022and receive and<br>50% off <span class="offer-brand">HOLLIVERS</span> fees</p>

  <div class="about-rule"></div>
  <div class="about">
    <h2 class="about-title">THINKING OF MOVING HOME?</h2>
    <p class="about-text">We have created an estate agency which offers a first class personal service with an honest and friendly approach. Having been open for only a year we have earned a name as one of the fastest growing estate agents in all Brighton &amp; Hove. Hollivers are extremely active in generating sales and achieving record breaking prices on premium properties in Hove. We have several serious buyers who are keen to purchase a property in the Hove area.</p>
  </div>

  <div class="contact-icons">
    <svg viewBox="0 0 24 24"><path d="M6.6 2.5l3 3.6-2 2.3c1.3 2.9 3.5 5.2 6.4 6.6l2.3-2 3.6 3-2 3.3C11 19 4.9 13 3.4 4.6z" fill="none" stroke="#fff" stroke-width="1.6" stroke-linejoin="round"/></svg>
    <svg viewBox="0 0 24 16"><rect x="1" y="1" width="22" height="14" fill="none" stroke="#fff" stroke-width="1.5"/><path d="M1 1l11 8 11-8M1 15l8-7M23 15l-8-7" fill="none" stroke="#fff" stroke-width="1.5"/></svg>
    <svg viewBox="0 0 24 24"><circle cx="12" cy="12" r="10" fill="none" stroke="#fff" stroke-width="1.4"/><ellipse cx="12" cy="12" rx="4.5" ry="10" fill="none" stroke="#fff" stroke-width="1.4"/><path d="M2 12h20M4 7h16M4 17h16" stroke="#fff" stroke-width="1.2"/></svg>
  </div>
  <div class="contact-box">
    <div class="contact-lines">
      <div class="contact-phone">01273 000 123</div>
      <div class="contact-line">sales@holliversestateagents.co.uk</div>
      <div class="contact-line">www.holliversestateagents.co.uk</div>
    </div>
  </div>

  <svg class="office-icon" viewBox="0 0 26 27"><path d="M1 26V1h12v25M13 9h11v17M0 26h26" fill="none" stroke="#fff" stroke-width="1.3"/><path d="M5 5h3v3H5zM5 11h3v3H5zM5 17h3v3H5zM17 13h2v2h-2zM17 18h2v2h-2z" fill="none" stroke="#fff" stroke-width="1"/></svg>
  <div class="info info--office">
    <div class="info-title">OUR OFFICE</div>
    <div>48 Harbour Rd, Hove, BN3 9ZZ</div>
  </div>
  <div class="info info--hours">
    <div class="info-title">OPENING TIMES</div>
    <div>Monday to Friday: 8.45am - 6:30pm</div>
    <div>Saturday: 8.45am - 5pm</div>
    <div>Sunday: By appointment only</div>
    <div>Open 7 days a week</div>
  </div>
</section>

<section class="page page--front" aria-label="Leaflet front">
  <div class="brand-name">HOLLIVERS</div>
  <h2 class="front-tagline">LET US<br>TREAT YOU<br>THIS CHRISTMAS</h2>
</section>

</body>
</html>
```